Asia based real estate financing firm needs and AWESOME design for a biz card -Harbor Lending Circle

Looking for a stylish, & corporate-looking business card for a real estate financing brokerage firm in Asia, offering global mortgage loans. I uploaded our current logos. We would like to add a splash of color (perhaps the house icon) or any other suggestions are open. For the winning designer, we have a lot of work! Thanks and best of luck!

Target Market(s)

Real estate investors globally. We want to look more like a BANK and NOT a real estate company. Please don't play up on a "house" design.

Industry/Entity Type

Banking

Contact Information for Business Card

Harbor Lending Circle
Peter Wilks
Co-Founder | Partner

14 Cassia Lane, Suite 310
Singapore 047219
www.hlc-example.asia
peterwilks@hlc-example.asia
+65 555-0142
WeChat: peterwilks

Colors

Designer to choose colors to be used in the design.

Requirements
Must have
• Must have the standard business requirements for a card; name, address, email, etc
• Can be horizontal or vertical.
Nice to have
• It would be great to see some sort of variation to the logo with a pop of color. Red is good as we're in Asia, however, other options work as well.
• Our tag line is - Borderless mortgages. It doesn't have to be on the card but might be nice.
• I'd like to start seeing our tagline within the cards as well. - Borderless mortgages.
• Also, please add our location. The location for this card is Singapore so perhaps it can be highlighted or emphasised in some way.
• Singapore | Hong Kong | Shanghai | Manila
• As we will soon open an office in Shanghai, having an option for both languages would be great.
Should not have
• I'm exceited and open to your creativity ... knock it out of the park!

```html
<!DOCTYPE html>
<html lang="en">
<head>
<meta charset="utf-8">
<title>Harbor Lending Circle — Business Card</title>
<link rel="stylesheet" href="https://fonts.googleapis.com/css2?family=Source+Serif+4:opsz,wght@8..60,400;8..60,700&display=swap">
<style>
  :root {
    --backdrop: #e8e8e8;
    --brand-red: #c01a27;
    --paper-white: #ffffff;
    --ink: #161616;
  }
  * { box-sizing: border-box; margin: 0; padding: 0; }
  html, body {
    width: 1200px;
    height: 800px;
    overflow: hidden;
    background: var(--backdrop);
    font-family: "Source Serif 4", Georgia, serif;
  }
  .canvas {
    position: relative;
    width: 1200px;
    height: 800px;
  }
  .card {
    position: absolute;
    top: 278px;
    width: 420px;
    height: 240px;
  }
  .card--front {
    left: 141px;
    background: var(--brand-red);
    display: flex;
    flex-direction: column;
    align-items: center;
    justify-content: center;
    gap: 14px;
    color: var(--paper-white);
  }
  .brand-mark {
    width: 12px;
    height: 12px;
    background: var(--paper-white);
  }
  .brand-name {
    font-weight: 400;
    text-transform: uppercase;
    color: var(--paper-white);
    text-align: center;
    line-height: 1.05;
  }
  .card--front .brand-name {
    font-size: 30px;
    letter-spacing: 2px;
  }
  .card--back {
    left: 637px;
    display: flex;
    background: var(--paper-white);
  }
  .back-brand {
    width: 182px;
    height: 100%;
    background: var(--brand-red);
    display: flex;
    flex-direction: column;
    align-items: center;
    justify-content: center;
    gap: 9px;
  }
  .back-brand .brand-mark {
    width: 8px;
    height: 8px;
  }
  .back-brand .brand-name {
    font-size: 15px;
    letter-spacing: 1px;
  }
  .contact {
    padding: 43px 0 0 21px;
    color: var(--ink);
    font-size: 13.6px;
    line-height: 16px;
  }
  .contact-name {
    font-weight: 700;
    font-size: 17px;
    line-height: 18px;
  }
  .contact-group + .contact-group {
    margin-top: 11px;
  }
  .contact p { white-space: nowrap; }
</style>
</head>
<body>
<main class="canvas">
  <section class="card card--front" aria-label="Card front">
    <span class="brand-mark" aria-hidden="true"></span>
    <p class="brand-name">Harbor Lending Circle</p>
  </section>

  <section class="card card--back" aria-label="Card back">
    <div class="back-brand">
      <span class="brand-mark" aria-hidden="true"></span>
      <p class="brand-name">Harbor<br>Lending Circle</p>
    </div>
    <div class="contact">
      <div class="contact-group">
        <p class="contact-name">Peter Wilks</p>
        <p class="contact-title">Co-Founder | Partner</p>
      </div>
      <div class="contact-group">
        <p>14 Cassia Lane, Suite 310</p>
        <p>Singapore 047219</p>
      </div>
      <div class="contact-group">
        <p>www.hlc-example.asia</p>
        <p>peterwilks@hlc-example.asia</p>
        <p>+65 555-0142</p>
        <p>WeChat: peterwilks</p>
      </div>
    </div>
  </section>
</main>
</body>
</html>
```